Website for IT consulting Company

I need a website upgrade, the existing site content is ok, I would also like to add a testimonial page, the site should be something that is easy for us to update content. You use the content from www.velmarketa.com as an example. I will also post update logo and artwork. I also need a contact form with some type of validation or captcha.

Please omit Address maps

Target Market(s)

small business, service oriented companies. We provide IT Consulting, support and mangement

Industry/Entity Type

Information Technology

Coding

Coded - Design and coding required

Number of Pages Required

1 page

Font styles to use
Serif
Sans Serif

Requirements
Must have
• Contain logo attached, and content from existing web site www.velmarketa.com.
• Also need to update content easily, and be movable to different platforms.
• There is a catch phrase
• "Let us worry about your technology…” “ so you don’t have to!”
• Should be included.
Nice to have
• Testimonial page, Project page where we can post new and past projects and pictures
Should not have
• none

```html
<!DOCTYPE html>
<html lang="en">
<head>
<meta charset="utf-8">
<title>Velmarketa – Flexible Solutions For Your Business Needs</title>
<link rel="stylesheet" href="https://fonts.googleapis.com/css2?family=Roboto:wght@400;500&family=Roboto+Condensed:wght@300;400;700&display=swap">
<style>
  :root {
    --hero-deep: #2f3d55;
    --hero-mid: #6d7f9c;
    --hero-light: #b9c6d8;
    --white: #ffffff;
    --ink: #333333;
    --muted: #5f6670;
    --bar-bg: #f1f2f4;
    --accent: #2f7fc8;
    --rule: #d9dde2;
    --chip: #9aa3ad;
  }
  * { box-sizing: border-box; margin: 0; padding: 0; }
  html, body { width: 1200px; height: 676px; overflow: hidden; background: var(--white); }
  body { font-family: "Roboto", Arial, sans-serif; color: var(--ink); }

  .site { width: 1200px; height: 676px; display: flex; flex-direction: column; }

  .hero {
    position: relative;
    height: 470px;
    color: var(--white);
  }
  .hero-photo {
    position: absolute; inset: 0;
    background:
      radial-gradient(ellipse at 70% 80%, rgba(120,160,215,.55), transparent 60%),
      radial-gradient(ellipse at 15% 70%, rgba(190,205,225,.5), transparent 55%),
      linear-gradient(180deg, var(--hero-deep) 0%, var(--hero-mid) 55%, var(--hero-light) 100%);
  }
  .site-header {
    position: relative;
    height: 70px;
    display: flex; align-items: center;
    padding: 0 40px;
    border-bottom: 1px solid rgba(255,255,255,.35);
  }
  .brand {
    display: flex; align-items: center; gap: 10px;
    font-family: "Roboto Condensed", Arial, sans-serif;
    font-weight: 700; font-size: 26px; letter-spacing: 1px;
    color: var(--white); text-transform: uppercase;
  }
  .brand-mark { width: 18px; height: 18px; background: var(--white); }
  .main-nav { display: flex; gap: 32px; margin-left: 80px; }
  .main-nav a {
    color: var(--white); text-decoration: none; font-size: 14px; letter-spacing: .3px;
  }
  .header-actions { margin-left: auto; display: flex; gap: 6px; }
  .btn-pill {
    font-size: 12px; font-weight: 500; padding: 7px 12px; border-radius: 16px;
    border: 1.5px solid var(--white); text-decoration: none;
  }
  .btn-login { color: var(--white); }
  .btn-contact { background: var(--white); color: var(--ink); }

  .hero-copy {
    position: relative;
    text-align: center;
    margin-top: 118px;
    font-family: "Roboto Condensed", Arial, sans-serif;
  }
  .hero-title { font-size: 26px; font-weight: 700; margin-bottom: 18px; }
  .hero-text { font-size: 11.5px; font-weight: 300; line-height: 1.35; }
  .btn-outline {
    display: inline-block; margin-top: 24px;
    font-size: 12px; color: var(--white); text-decoration: none;
    border: 1.5px solid var(--white); border-radius: 4px; padding: 7px 15px;
  }
  .slider-dots {
    position: absolute; bottom: 12px; left: 50%; transform: translateX(-50%);
    display: flex; gap: 8px;
  }
  .slider-dots span { width: 8px; height: 8px; border-radius: 50%; background: var(--white); }
  .slider-dots span.is-idle { background: transparent; border: 1.5px solid var(--white); }

  .contact-bar {
    height: 34px; background: var(--bar-bg);
    display: flex; align-items: center; padding: 0 40px 0 40px;
    font-size: 12.5px; color: var(--muted);
  }
  .contact-item { display: flex; align-items: center; gap: 7px; margin-right: 26px; }
  .social { margin-left: auto; display: flex; align-items: center; gap: 16px; }
  .social-chip { width: 16px; height: 16px; background: var(--chip); border-radius: 2px; }

  .intro {
    flex: 1; display: flex; align-items: center; padding: 0 40px;
  }
  .intro-brand { width: 400px; text-align: center; }
  .intro-logo {
    display: inline-flex; align-items: center; gap: 10px;
    font-family: "Roboto Condensed", Arial, sans-serif; font-weight: 700;
    font-size: 34px; color: var(--accent); text-transform: uppercase; letter-spacing: 1px;
  }
  .intro-logo .brand-mark { width: 24px; height: 24px; background: var(--accent); }
  .catch-phrase { font-size: 8px; color: var(--accent); margin-top: 2px; }
  .intro-rule { border-top: 1.5px dashed var(--accent); margin: 10px 0 14px; }
  .intro-note { font-size: 12.5px; }
  .intro-divider { width: 2px; height: 84px; background: var(--accent); margin: 0 22px 0 12px; }
  .intro-text { flex: 1; text-align: center; font-size: 11.5px; line-height: 1.5; }
</style>
</head>
<body>
<div class="site">
  <section class="hero">
    <div class="hero-photo" role="img" aria-label="Blurred office desk with a glass of water, eyeglasses and a printed blue bar chart"></div>
    <header class="site-header">
      <div class="brand"><span class="brand-mark"></span>Velmarketa</div>
      <nav class="main-nav">
        <a href="#">ABOUT</a><a href="#">SUPPORT</a><a href="#">CLIENTS</a><a href="#">PROJECT</a><a href="#">CAREERS</a>
      </nav>
      <div class="header-actions">
        <a class="btn-pill btn-login" href="#">Log In</a>
        <a class="btn-pill btn-contact" href="#">Contact Us</a>
      </div>
    </header>
    <div class="hero-copy">
      <h1 class="hero-title">Flexible Solutions For Your Business Needs</h1>
      <p class="hero-text">
        Velmarketa is a technology solution provider based in Houston,Texas.<br>
        Our goal is to make technology a non-issue for individuals and small to medium size businesses ranging from 5 to 150 Users.<br>
        Velmarketa has the experience, the tools, high-level technology solutions and training to power your business and your work force.<br>
        We understand that all business's have one goal in common!
      </p>
      <a class="btn-outline" href="#">Learn More</a>
    </div>
    <div class="slider-dots"><span></span><span class="is-idle"></span><span></span></div>
  </section>

  <div class="contact-bar">
    <span class="contact-item">
      <svg width="12" height="12" viewBox="0 0 24 24" fill="currentColor"><path d="M6.6 10.8a15 15 0 0 0 6.6 6.6l2.2-2.2a1 1 0 0 1 1-.25 11.4 11.4 0 0 0 3.6.57 1 1 0 0 1 1 1V20a1 1 0 0 1-1 1A17 17 0 0 1 3 4a1 1 0 0 1 1-1h3.5a1 1 0 0 1 1 1c0 1.25.2 2.45.57 3.57a1 1 0 0 1-.25 1z"/></svg>
      +1 800 555 01 47
    </span>
    <span class="contact-item">
      <svg width="13" height="10" viewBox="0 0 26 20" fill="currentColor"><path d="M0 0h26v20H0z" opacity=".85"/><path d="M1 1l12 10L25 1" stroke="#f1f2f4" stroke-width="2" fill="none"/></svg>
      hello@velmarketa.com
    </span>
    <div class="social">
      <span class="social-chip"></span><span class="social-chip"></span><span class="social-chip"></span>
      <svg width="12" height="12" viewBox="0 0 24 24" fill="none" stroke="currentColor" stroke-width="3"><circle cx="10" cy="10" r="7"/><path d="M15 15l7 7"/></svg>
    </div>
  </div>

  <section class="intro">
    <div class="intro-brand">
      <div class="intro-logo"><span class="brand-mark"></span>Velmarketa</div>
      <p class="catch-phrase">Let us worry about your technology… So you don't have to!</p>
      <div class="intro-rule"></div>
      <p class="intro-note">Outsourcing became part of the business lexicon during the 1980s</p>
    </div>
    <div class="intro-divider"></div>
    <p class="intro-text">
      Outsourcing is subcontracting a process, such as product design or manufacturing, to a third-party company.[1] The decision to outsource is often made in the interest of lowering firm costs, redirecting or conserving energy directed at the competencies of a particular business, or to make more efficient use of land, labor, capital, (information) technology and resources
    </p>
  </section>
</div>
</body>
</html>
```